Content processing platform needs a landing page for products

We need a general landing page for products that we are launching. The concept of the product page is to do two things: a) Get users to sign up for our waitlist (que) so they get access to the product (we give access weekly). b) To generate interest for future products that we have not decided on yet. Mockups: Please see our mockups for inspiration. You have pretty free hands to combine, but please don't let our users think :-). Style: Please use the colours of our style sheet and see the home page (penlyhub.com) for inspiration on how we want the style and tone to be. The final design should communicate "scaling".

Target Market(s)

B2B - online businesses big and small that wish to scale their production of content and translation.

Industry/Entity Type

SaaS

Number of Pages Required

1 page

Font styles to use
Other font styles liked:
• open sans

Requirements
Must have
• Follow our styleguide.

```html
<!DOCTYPE html>
<html lang="en">
<head>
<meta charset="utf-8">
<title>Penlyhub – Content Processing Platform</title>
<link rel="stylesheet" href="https://fonts.googleapis.com/css2?family=Open+Sans:wght@300;400;600;700;800&display=swap">
<style>
:root{
  --cyan:#19aee6;
  --cyan-dark:#1592c4;
  --teal:#2fc7c9;
  --pink:#f7345e;
  --mint:#3ee8b5;
  --navy:#2c3f7c;
  --ink:#333a40;
  --muted:#777e85;
  --light:#f3f5f6;
  --card:#f7f7f7;
  --footer:#2b2b2b;
  --bar:#1d3450;
  --white:#ffffff;
}
*{box-sizing:border-box;margin:0;padding:0}
html,body{width:1200px;height:5085px;overflow:hidden}
body{font-family:"Open Sans",Arial,sans-serif;color:var(--ink);background:var(--white);position:relative}
section,header,footer{position:absolute;left:0;width:1200px}
.abs{position:absolute}

/* hero */
.hero{top:0;height:712px;background:linear-gradient(135deg,var(--cyan) 0%,#22b8dd 55%,var(--teal) 100%);overflow:hidden;color:var(--white)}
.hero-wave{position:absolute;left:0;bottom:0;width:1200px;height:160px}
.brand{left:100px;top:32px;font-size:32px;font-weight:800;letter-spacing:-.5px}
.nav{left:395px;top:46px;display:flex;gap:26px;font-size:17px;font-weight:600;text-transform:uppercase}
.btn-signin{left:890px;top:27px;width:215px;height:56px;background:var(--white);color:var(--cyan);font-weight:600;font-size:18px;display:flex;align-items:center;justify-content:center}
.hero-title{left:100px;top:228px;font-size:38px;line-height:58px;font-weight:800;text-transform:uppercase;white-space:nowrap}
.hero-title .hl{color:var(--mint)}
.btn{background:var(--pink);color:var(--white);font-weight:600;display:flex;align-items:center;justify-content:center}
.btn-learn{left:100px;top:505px;width:215px;height:56px;font-size:19px}
.hero-visual{left:620px;top:225px;width:490px;height:345px;border-radius:14px;background:linear-gradient(160deg,rgba(255,255,255,.85),rgba(255,255,255,.55))}

/* stats */
.stats{top:712px;height:200px}
.trophy{left:100px;top:52px}
.trust-title{left:195px;top:58px;font-size:32px;font-weight:700}
.trust-sub{left:195px;top:104px;font-size:18px;color:var(--muted)}
.stat{top:58px;text-align:center}
.stat b{display:block;font-size:36px;font-weight:600;color:var(--cyan-dark);letter-spacing:1px}
.stat span{font-size:18px;color:var(--muted)}

/* value cards */
.values{top:932px;height:380px}
.value-card{top:8px;width:318px;height:355px;background:var(--card);border-bottom:6px solid;border-image:linear-gradient(90deg,var(--pink),var(--cyan)) 1;padding:140px 30px 0}
.value-icon{position:absolute;left:30px;top:50px}
.value-card h3{font-size:22px;font-weight:400;margin-bottom:28px}
.value-card p{font-size:15px;line-height:24px;color:var(--muted)}

/* signup */
.signup{top:1390px;height:730px;background:linear-gradient(115deg,#2a4f8e 0%,#3b4d8b 45%,#a3406e 80%,#d8395e 100%);color:var(--white)}
.signup-title{left:100px;top:148px;font-size:44px;line-height:56px;font-weight:400}
.signup-lead{left:100px;top:300px;width:470px;font-size:26px;line-height:38px}
.signup-list{left:138px;top:446px;list-style:none;font-size:26px;line-height:50px}
.signup-list li{position:relative}
.signup-list li::before{content:"";position:absolute;left:-38px;top:17px;width:18px;height:18px;background:var(--white)}
.form{left:600px;top:60px;width:505px}
.form h2{text-align:center;font-size:44px;font-weight:600;letter-spacing:1px}
.form .have{text-align:center;font-size:17px;margin:6px 0 28px}
.form .have a{color:var(--mint)}
.field{height:58px;background:rgba(20,25,45,.45);margin-bottom:20px;font-size:18px;padding:0 24px;display:flex;align-items:center;justify-content:space-between}
.row{display:flex;gap:20px}.row .field{flex:1}
.terms{display:flex;gap:18px;font-size:13px;margin:-4px 0 22px;align-items:center}
.terms a{color:var(--mint)}
.btn-signup{height:66px;font-size:26px;text-transform:uppercase}

/* benefits */
.benefits{top:2120px;height:846px}
.benefit-photo{left:100px;top:130px;width:400px;height:565px;background:linear-gradient(160deg,#5a6b78,#2f3b47 60%,#8b6f4e)}
.benefit{left:600px;width:510px}
.benefit svg{position:absolute;left:0;top:0}
.benefit h4{margin-left:130px;font-size:22px;font-weight:400;margin-bottom:12px}
.benefit p{margin-left:130px;font-size:16px;line-height:25px;color:var(--muted)}

/* pricing */
.pricing{top:2966px;height:1068px;background:var(--light);text-align:center}
.pricing h2{position:absolute;left:0;width:1200px;top:110px;font-size:44px;font-weight:400}
.pricing .sub{position:absolute;left:0;width:1200px;top:188px;font-size:20px;color:var(--ink)}
.plan{top:322px;width:318px;height:625px;border:4px solid #444;background:var(--white);padding-top:40px}
.plan.featured{border-color:var(--cyan)}
.plan h3{font-size:30px;font-weight:400}
.plan .price{font-size:92px;font-weight:300;color:var(--cyan);line-height:1.3;margin-top:22px}
.plan .per{font-size:16px;color:var(--muted)}
.plan hr{border:0;border-top:2px solid #999;width:275px;margin:52px auto 34px}
.plan ul{list-style:none;font-size:18px;line-height:45px}
.plan .btn{width:188px;height:56px;margin:28px auto 0;font-size:19px;background:#555}
.plan.featured .btn{background:var(--pink)}

/* clients */
.clients{top:4034px;height:480px;text-align:center}
.clients h2{position:absolute;left:0;width:1200px;top:124px;font-size:44px;font-weight:400}
.client-row{position:absolute;left:100px;top:220px;width:1005px;display:flex;justify-content:space-between;align-items:center}
.client{display:flex;align-items:center;gap:10px;font-size:32px;font-weight:600;color:#6d7378}
.client i{width:22px;height:22px;background:#6d7378;display:block}

/* footer */
.footer{top:4510px;height:456px;background:var(--footer);color:#e8e8e8}
.cta{left:295px;top:4405px;width:605px;height:220px;background:#0aa6e6;color:var(--white);text-align:center;padding-top:40px;z-index:2;position:absolute}
.cta h2{font-size:40px;font-weight:400}
.cta p{font-size:19px;margin:8px 0 26px}
.cta .reg{display:inline-block;background:#1e1e1e;padding:10px 30px;font-size:17px}
.links{top:200px;list-style:none;font-size:18px;line-height:31px}
.links .on{color:var(--cyan);text-decoration:underline}
.bar{top:4966px;height:119px;background:var(--bar);color:#dfe6ee}
.socials{left:100px;top:44px;display:flex;gap:16px}
.socials span{width:34px;height:34px;background:var(--cyan);display:block}
.copy{right:95px;top:48px;font-size:18px}
</style>
</head>
<body>

<header class="hero">
  <div class="abs brand">Penlyhub</div>
  <nav class="abs nav"><span>Browse</span><span>Training</span><span>Blog</span><span>We're hiring!</span></nav>
  <div class="abs btn-signin">Sign In Now</div>
  <h1 class="abs hero-title">Manage your<br><span class="hl">content</span> with our new<br>content <span class="hl">processing</span><br><span class="hl">platform</span></h1>
  <div class="abs btn btn-learn">Learn More</div>
  <div class="abs hero-visual" role="img" aria-label="Illustration of a phone and laptop showing the platform"></div>
  <svg class="hero-wave" viewBox="0 0 1200 160" preserveAspectRatio="none" aria-hidden="true">
    <path d="M0 90 C200 20 380 140 600 90 C820 40 980 130 1200 60 L1200 160 L0 160Z" fill="#ffffff" opacity=".35"/>
    <path d="M0 120 C240 60 420 160 640 115 C860 70 1000 150 1200 100 L1200 160 L0 160Z" fill="#ffffff"/>
  </svg>
</header>

<section class="stats">
  <svg class="abs trophy" width="70" height="70" viewBox="0 0 70 70" aria-hidden="true"><path d="M18 8h34v18a17 17 0 0 1-34 0z" fill="none" stroke="#333a40" stroke-width="3"/><path d="M18 14H6c0 12 6 18 14 18M52 14h12c0 12-6 18-14 18" fill="none" stroke="#333a40" stroke-width="3"/><path d="M35 43v12M22 62h26" stroke="#f7345e" stroke-width="4"/></svg>
  <div class="abs trust-title">Trusted by 4000+</div>
  <div class="abs trust-sub">High performing team worldwide</div>
  <div class="abs stat" style="left:605px"><b>0035984</b><span>Downloads</span></div>
  <div class="abs stat" style="left:810px"><b>00359+</b><span>Active Installs</span></div>
  <div class="abs stat" style="left:980px"><b>0035984</b><span>Paid Users</span></div>
</section>

<section class="values">
  <article class="abs value-card" style="left:100px">
    <svg class="value-icon" width="90" height="60" viewBox="0 0 90 60" aria-hidden="true"><rect x="2" y="2" width="80" height="46" fill="none" stroke="#f7345e" stroke-width="3"/><path d="M30 58h24" stroke="#333a40" stroke-width="3"/><text x="24" y="33" font-size="20" font-family="Open Sans,sans-serif" fill="#333a40">$$</text></svg>
    <h3>Cheaper</h3><p>Lorem ipsum dolor sit amet, consectetur adipiscing elit, sed do eiusmod tempor.</p>
  </article>
  <article class="abs value-card" style="left:445px">
    <svg class="value-icon" width="70" height="70" viewBox="0 0 70 70" aria-hidden="true"><path d="M60 10L30 40M60 10L50 45 30 40 25 20z" fill="none" stroke="#333a40" stroke-width="3"/><path d="M14 56l12-12" stroke="#f7345e" stroke-width="4"/></svg>
    <h3>Faster</h3><p>Lorem ipsum dolor sit amet, consectetur adipiscing elit, sed do eiusmod tempor.</p>
  </article>
  <article class="abs value-card" style="left:790px">
    <svg class="value-icon" width="90" height="70" viewBox="0 0 90 70" aria-hidden="true"><rect x="2" y="2" width="84" height="60" fill="none" stroke="#333a40" stroke-width="3"/><path d="M2 14h84" stroke="#f7345e" stroke-width="3"/><circle cx="34" cy="40" r="11" fill="none" stroke="#333a40" stroke-width="3"/><circle cx="58" cy="44" r="8" fill="none" stroke="#333a40" stroke-width="3"/></svg>
    <h3>Automated</h3><p>Lorem ipsum dolor sit amet, consectetur adipiscing elit, sed do eiusmod tempor.</p>
  </article>
</section>

<section class="signup">
  <h2 class="abs signup-title">Get Ready to New<br>Product Access</h2>
  <p class="abs signup-lead">Lorem ipsum dolor sit amet, consectetur adipiscing elit, sed do eiusmod tempor incididunt ut labore.</p>
  <ul class="abs signup-list"><li>Tempor incididunt ut labore.</li><li>Tempor incididunt.</li><li>Tempor incididunt ut labore.</li></ul>
  <form class="abs form">
    <h2>SIGN UP</h2>
    <p class="have">Already have an account? <a>Sign in</a></p>
    <div class="field">Email address</div>
    <div class="row"><div class="field">First Name</div><div class="field">Last Name</div></div>
    <div class="field">Native Language <svg width="26" height="22" viewBox="0 0 26 22" aria-hidden="true"><path d="M2 2h22L13 20z" fill="none" stroke="#fff" stroke-width="2"/></svg></div>
    <div class="field">Password</div>
    <div class="terms"><svg width="20" height="16" viewBox="0 0 20 16" aria-hidden="true"><path d="M2 8l6 6L18 2" fill="none" stroke="#fff" stroke-width="2"/></svg><span>By signing up, you confirm that you have read and agreed to our<br><a>terms of service</a></span></div>
    <div class="btn btn-signup">Sign Up</div>
  </form>
</section>

<section class="benefits">
  <div class="abs benefit-photo" role="img" aria-label="Photo of a businessman presenting in an office, brand tile in the corner"></div>
  <div class="abs benefit" style="top:125px">
    <svg width="80" height="76" viewBox="0 0 80 76" aria-hidden="true"><path d="M6 70h68M14 60V48M28 60V40M42 60V32M56 60V22" stroke="#1aa2d6" stroke-width="4"/><path d="M8 40L30 22 44 30 70 8" fill="none" stroke="#333a40" stroke-width="3"/></svg>
    <h4>Hack your growth</h4><p>Lorem ipsum dolor sit amet, consectetur and adipiscing elit, sed do eiusmod tempor.</p>
  </div>
  <div class="abs benefit" style="top:280px">
    <svg width="80" height="76" viewBox="0 0 80 76" aria-hidden="true"><rect x="24" y="8" width="34" height="58" fill="none" stroke="#1aa2d6" stroke-width="3"/><rect x="32" y="22" width="18" height="22" fill="none" stroke="#333a40" stroke-width="3"/></svg>
    <h4>Well Documented</h4><p>Lorem ipsum dolor sit amet, consectetur and adipiscing elit, sed do eiusmod tempor.</p>
  </div>
  <div class="abs benefit" style="top:430px">
    <svg width="80" height="76" viewBox="0 0 80 76" aria-hidden="true"><path d="M20 34a20 20 0 0 1 40 0" fill="none" stroke="#1aa2d6" stroke-width="3"/><rect x="14" y="32" width="10" height="16" fill="#1aa2d6"/><rect x="56" y="32" width="10" height="16" fill="#1aa2d6"/><path d="M16 72c4-12 44-12 48 0" fill="none" stroke="#333a40" stroke-width="3"/></svg>
    <h4>24/7 Support</h4><p>Lorem ipsum dolor sit amet, consectetur and adipiscing elit, sed do eiusmod tempor.</p>
  </div>
  <div class="abs benefit" style="top:580px">
    <svg width="80" height="76" viewBox="0 0 80 76" aria-hidden="true"><circle cx="40" cy="38" r="28" fill="none" stroke="#1aa2d6" stroke-width="3" stroke-dasharray="10 5"/><circle cx="40" cy="38" r="12" fill="none" stroke="#333a40" stroke-width="3"/></svg>
    <h4>Life time update</h4><p>Lorem ipsum dolor sit amet, consectetur and adipiscing elit, sed do eiusmod tempor.</p>
  </div>
</section>

<section class="pricing">
  <h2>Explore more features by selecting a plan</h2>
  <p class="sub">Choose the best solution for your business.</p>
  <article class="abs plan" style="left:100px">
    <h3>Free</h3><div class="price">$0</div><div class="per">per month</div><hr>
    <ul><li>Basic support on RepoDock</li><li>Monthly updates</li><li>Free cancelation</li></ul>
    <div class="btn">Start Free</div>
  </article>
  <article class="abs plan featured" style="left:445px">
    <h3>Multiple Use</h3><div class="price">$49</div><div class="per">per month</div><hr>
    <ul><li>Basic support on RepoDock</li><li>Monthly updates</li><li>Free cancelation</li></ul>
    <div class="btn">Start Free</div>
  </article>
  <article class="abs plan" style="left:790px">
    <h3>Extended Use</h3><div class="price">$199</div><div class="per">per month</div><hr>
    <ul><li>Basic support on RepoDock</li><li>Monthly updates</li><li>Free cancelation</li></ul>
    <div class="btn">Start Free</div>
  </article>
</section>

<section class="clients">
  <h2>Trusted by over 10000 clients</h2>
  <div class="client-row">
    <span class="client"><i></i>Quorvex</span>
    <span class="client">Zentrofy</span>
    <span class="client">Corvany</span>
    <span class="client">Paydrix</span>
    <span class="client"><i></i>Shopvelle</span>
  </div>
</section>

<footer class="footer">
  <ul class="abs links" style="left:110px"><li class="on">- About Us</li><li>- Team</li><li>- Contact</li><li>- Terms of Service</li><li>- Privacy Policy</li><li>- Imprint</li></ul>
  <ul class="abs links" style="left:480px"><li>- Penlyhub Affiliate</li><li>- Careers</li><li>- Developer Resources</li><li>- Penlyhub Workshops</li><li>- Help</li></ul>
  <ul class="abs links" style="left:840px"><li>Penlyhub B.V.</li><li>Havenkade 14 1011 AB</li><li>Meerdorp The Netherlands</li><li>Tel: +31 (0)20 000 1234</li><li>VAT: NL000000000B01</li></ul>
</footer>

<div class="cta">
  <h2>We build it. You rock it.</h2>
  <p>A complete and customizable solution to your dreams.</p>
  <span class="reg">Register Now</span>
</div>

<footer class="bar">
  <div class="abs socials" aria-label="Social links"><span></span><span></span><span></span><span></span><span></span></div>
  <div class="abs copy">© 2018 Penlyhub. All Rights Reserved.</div>
</footer>

</body>
</html>
```